New Alcoholic Spiked Seltzer Line

We need a can design for a line of low calorie alcoholic seltzer. This product is a sparkling water and vodka drink with no sugar added in a slim 12 oz can.

This is a lighter, healthier, alternative to the sugary ready-to-drinks on the market. The product contains only 3 ingredients: Vodka, Water and Natural Flavors. It has only 100 calories but still has 5% alcohol, so you don't need to sacrifice alcohol to cut calories.

This product also does not contain any preservatives.

We want this design to communicate the following objectives to the consumer and in this order:

1. Appetizing product
2.Low calorie
3.Communicate the type of beverage (Spiked Seltzer)

The brand name of the product is VELKA.

The flavor of the product needed to be used for the design is Mango-Orange.

Comparable products are:

www.brisavelfizz.example/
https://www.tarnowbubble.example
https://quellrind.example/

The designs should not infringe or copy the creative directions of the products mentionned above. They are only given so that you can better understand the type of product we are developing.

Target Market(s)

Young Professional women between the ages of 25 and 44

Industry/Entity Type

Product

Colors

Designer to choose colors to be used in the design.

Requirements
Must have
• Design extendibility, meaning it can be adapted for other flavors.
• This is a new category in the market we are targeting, so consumers must easily be able to identify what type of product this is.

```html
<!DOCTYPE html>
<html lang="en">
<head>
<meta charset="utf-8">
<title>VELKA Mango-Orange Alcoholic Seltzer – Can Label</title>
<link rel="stylesheet" href="https://fonts.googleapis.com/css2?family=Fira+Sans:wght@400;700;800&display=swap">
<style>
  :root {
    --backdrop: #eef0ed;
    --label-white: #f7f6f1;
    --mango: #f2a516;
    --mango-deep: #ee8a0c;
    --sunrise: #f9c53b;
    --brand-red: #e33a4f;
    --coral: #e77e76;
    --ink-soft: #c9a08e;
    --seltzer-text: #d8902a;
  }
  * { box-sizing: border-box; margin: 0; padding: 0; }
  html, body {
    width: 1200px; height: 689px; overflow: hidden;
    background: var(--backdrop);
    font-family: "Fira Sans", "Helvetica Neue", Arial, sans-serif;
  }
  .canvas {
    position: relative; width: 1200px; height: 689px;
    background: radial-gradient(ellipse at 50% 40%, #fbfbf9 0%, var(--backdrop) 75%);
  }
  .can-label {
    position: absolute; left: 490px; top: 44px;
    width: 220px; height: 590px;
    background: var(--label-white);
    overflow: hidden;
    text-align: center;
  }
  .top-band {
    position: absolute; left: 0; top: 0; width: 100%; height: 44px;
    background: linear-gradient(180deg, var(--mango-deep) 0%, var(--sunrise) 50%, rgba(249,197,59,0) 100%);
  }
  .brand-name {
    position: absolute; left: 0; top: 124px; width: 100%;
    font-size: 54px; font-weight: 800; letter-spacing: 3px;
    color: var(--brand-red);
    line-height: 1;
  }
  .brand-dot {
    display: inline-block; width: 10px; height: 10px;
    background: var(--brand-red); border-radius: 50%;
    vertical-align: middle; margin-left: 4px;
  }
  .claim-rule {
    position: absolute; left: 76px; top: 296px; width: 68px; height: 1px;
    background: var(--ink-soft);
  }
  .claim {
    position: absolute; left: 0; top: 304px; width: 100%;
    font-size: 11.5px; font-weight: 400; letter-spacing: 0.4px;
    color: var(--coral);
  }
  .flavor {
    position: absolute; left: 0; top: 364px; width: 100%;
    font-size: 27px; font-weight: 800; line-height: 28px;
    color: var(--mango);
    letter-spacing: 0.3px;
  }
  .product-type {
    position: absolute; left: 0; top: 437px; width: 100%;
    font-size: 13px; font-weight: 400; letter-spacing: 0.3px;
    color: var(--seltzer-text);
  }
  .fizz-area {
    position: absolute; left: 0; bottom: 0; width: 100%; height: 132px;
    background: linear-gradient(180deg, rgba(247,246,241,0) 0%, #efe6cf 30%, var(--sunrise) 62%, var(--mango-deep) 100%);
  }
</style>
</head>
<body>
  <main class="canvas">
    <section class="can-label" aria-label="VELKA Mango-Orange Alcoholic Seltzer can label">
      <div class="top-band"></div>
      <h1 class="brand-name">VELKA<span class="brand-dot"></span></h1>
      <div class="claim-rule"></div>
      <p class="claim">LOW CALORIE</p>
      <h2 class="flavor">MANGO-<br>ORANGE</h2>
      <p class="product-type">Alcoholic Seltzer</p>
      <div class="fizz-area" role="img" aria-label="Sparkling bubbles rising through mango-orange seltzer"></div>
    </section>
  </main>
</body>
</html>
```